LAW FIRM - RE-DESIGN - (professional, excellence, tradition and innovation)

We are a premier law firm in New South Wales, Australia. We pride ourselves on being cutting edge and up to date in our market.

Our firm formed in 1874 and has a particularly strong tradition within it's geographic footprint. acting for clients over multiple generations. Despite our regional background, our reputation for excellence has enable us to remain highly visible in a large area.

We have invested heavily in ensuring future planning of this business, and do so on a recurring basis. This has lead to a review of our existing web site.

Although serviceable we feel our previous website is out-of-date and not as in touch with the modern market. We are aware that for the emerging clients a web site is often the face of a firm and a failure to hold attention on the first page may fail to capture the client.

We are seeking designs to communicate the core values of professionalism and excellence. At the same time as maintaining traditional country values of honesty, integrity and hard work we strive to embrace changes to the law and technology.

Target Market(s)

Clients of Law Firm

Industry/Entity Type

Law Firm

Coding

Coded - Design and coding required

Number of Pages Required

5+ page

Requirements
Must have
• A strong sense of professionalism and excellence with a careful balance between traditional values and innovation.
Nice to have
• We have included within our design brief links to top competitors sites to assist for design concepts.

```html
<!DOCTYPE html>
<html lang="en">
<head>
<meta charset="utf-8">
<title>HBM Law</title>
<link rel="stylesheet" href="https://fonts.googleapis.com/css2?family=Tinos:ital,wght@0,400;0,700;1,400&family=Open+Sans:wght@400;600;700&display=swap">
<style>
:root{
  --navy:#123f7d;
  --navy-deep:#0c2f63;
  --ink:#333;
  --muted:#666;
  --rule:#9aa3b0;
  --band-grey:#ececec;
  --white:#fff;
}
*{margin:0;padding:0;box-sizing:border-box}
html,body{width:1200px;height:3782px;overflow:hidden}
body{position:relative;background:var(--white);font-family:"Open Sans",Arial,sans-serif;color:var(--ink)}
.abs{position:absolute}
h2{font-weight:400}

/* header */
.site-header{left:0;top:0;width:1200px;height:81px;background:var(--white)}
.brand{left:100px;top:12px;font-family:"Tinos",serif;font-size:38px;line-height:56px;color:var(--navy);font-weight:400;letter-spacing:1px}
.main-nav{right:90px;top:32px;display:flex;gap:58px;font-family:"Tinos",serif;font-size:14px;letter-spacing:.5px;color:#222;text-transform:uppercase}
.main-nav span.has-sub::after{content:"\2304";font-size:10px;margin-left:4px;position:relative;top:-3px}

/* hero */
.hero{left:0;top:81px;width:1200px;height:499px;background:linear-gradient(180deg,#7fb4e6 0%,#a9cdee 35%,#6e8aa0 58%,#2f5c7f 78%,#1f4864 100%)}
.hero-title{left:100px;top:440px;font-family:"Tinos",serif;font-size:40px;color:var(--white);letter-spacing:1px}
.hero-sub{left:100px;top:490px;font-family:"Tinos",serif;font-style:italic;font-size:31px;color:var(--white)}
.dots{display:flex;gap:8px}
.dots i{width:9px;height:9px;border-radius:50%;background:rgba(255,255,255,.55);display:block}
.dots i.on{background:#fff}

/* section titles */
.section-title{width:1200px;left:0;text-align:center;font-family:"Tinos",serif;font-size:32px;font-weight:400;letter-spacing:1px;text-transform:uppercase;color:#333}
.title-rule{width:40px;height:2px;background:var(--rule);left:580px}
.intro{left:200px;width:800px;text-align:center;font-size:12.5px;line-height:26px;color:var(--muted)}

/* practice */
.area-photo{width:324px;height:202px}
.area-title{font-family:"Tinos",serif;font-size:19px;color:#333;text-transform:uppercase}
.area-text{width:300px;font-size:13px;line-height:26px;color:var(--muted)}
.btn{height:40px;border-radius:20px;font-family:"Tinos",serif;font-size:13px;text-transform:uppercase;display:flex;align-items:center;justify-content:center;letter-spacing:.5px}
.btn-solid{background:var(--navy);color:var(--white)}
.btn-line{border:1px solid rgba(255,255,255,.8);color:var(--white)}

/* about */
.about-photo{left:0;top:1553px;width:600px;height:403px;background:linear-gradient(135deg,#8d6f52 0%,#5a4232 45%,#2e2a2a 75%,#bfb3a3 100%)}
.about-band{left:600px;top:1553px;width:600px;height:403px;background:var(--navy)}
.about-title{right:90px;top:1630px;font-family:"Tinos",serif;font-size:34px;font-weight:400;color:var(--white);text-transform:uppercase}
.about-text{right:90px;top:1690px;width:440px;text-align:right;font-size:12px;line-height:25px;color:#e3e9f3}

/* cases */
.case-title{width:310px;font-family:"Tinos",serif;font-size:16px;line-height:26px;text-transform:uppercase;color:#333}
.case-rule{width:34px;height:2px;background:var(--rule)}

/* partners */
.partners{left:0;top:2506px;width:1200px;height:477px;background:linear-gradient(90deg,#1f2124 0%,#3a3c40 45%,#26282b 100%)}
.partner{width:170px;text-align:center}
.partner .ring{width:110px;height:110px;border-radius:50%;border:3px solid var(--navy);margin:0 auto;background:linear-gradient(180deg,#c9b7a4,#6d7480)}
.partner .name{margin-top:24px;font-size:13px;font-weight:700;color:var(--white);text-transform:uppercase}

/* testimonials */
.testimonials{left:0;top:2983px;width:1200px;height:471px;background:var(--band-grey)}
.client-photo{left:157px;top:3195px;width:190px;height:190px;border-radius:50%;border:5px solid #fff;background:linear-gradient(180deg,#d9d4cc,#8a8a8e)}
.quote{left:449px;top:3233px;width:560px;font-style:italic;font-size:12.5px;line-height:24px;color:#8a8f98}
.qmark{font-family:"Tinos",serif;font-size:44px;color:#b5b9c0;line-height:1}

/* footer */
.site-footer{left:0;top:3454px;width:1200px;height:265px;background:var(--navy)}
.foot-head{font-family:"Tinos",serif;font-size:15px;color:var(--white);text-transform:uppercase;letter-spacing:.5px}
.foot-text{font-size:12px;line-height:24px;color:#dbe3f0}
.foot-list{list-style:none;font-size:12px;line-height:27px;color:#dbe3f0}
.foot-brand{left:958px;top:3520px;font-family:"Tinos",serif;font-size:60px;color:rgba(255,255,255,.55)}
.bottom-bar{left:0;top:3719px;width:1200px;height:63px;background:var(--navy-deep);font-size:11.5px;color:#cfd8e6}
.social{display:flex;gap:14px;align-items:center}
.social i{width:14px;height:14px;border-radius:50%;background:rgba(255,255,255,.75);display:block}
</style>
</head>
<body>

<header class="abs site-header">
  <div class="abs brand">HBM Law</div>
  <nav class="abs main-nav">
    <span>Home</span><span class="has-sub">About Us</span><span class="has-sub">Services</span><span class="has-sub">People</span><span>Community</span><span>Contact Us</span>
  </nav>
</header>

<section class="abs hero" role="img" aria-label="Harbour city skyline with opera house on the water under a clear blue sky"></section>
<div class="abs hero-title">HBM LAW</div>
<div class="abs hero-sub">We are a premier law firm in New South Wales, Australia</div>
<div class="abs dots" style="left:572px;top:542px"><i class="on"></i><i></i><i></i><i></i></div>

<h2 class="abs section-title" style="top:660px">Welcome to HBM Law</h2>
<div class="abs title-rule" style="top:712px"></div>
<p class="abs intro" style="top:742px">HBM Law has been in existence since 1874 originally starting out as the firm Walter Greaves of Ashford Vale. In 1894 Walter Greaves was acquired by Colonel RT Hartley. The firm became known as RT Hartley &amp; Co. until early 1970 when it became Hartley &amp; Co, Hartley Brennan &amp; Co in 1979 and Hartley Brennan &amp; Moss in 1982.</p>

<h2 class="abs section-title" style="top:895px">Practice Areas</h2>
<div class="abs title-rule" style="top:947px"></div>
<p class="abs intro" style="top:970px">HBM Law has been in existence since 1874 originally starting out as the firm Walter Greaves of Ashford Vale.</p>

<div class="abs area-photo" style="left:100px;top:1039px;background:linear-gradient(180deg,#5a93d6,#9cc3ea 55%,#8d8a84)" role="img" aria-label="Building under construction with a crane against blue sky"></div>
<div class="abs area-photo" style="left:439px;top:1039px;background:linear-gradient(135deg,#1d3d62,#5a88b5 50%,#24476c)" role="img" aria-label="Glass corporate office towers seen from below"></div>
<div class="abs area-photo" style="left:776px;top:1039px;background:linear-gradient(135deg,#8e2b24,#b8473a 55%,#d8c9b8)" role="img" aria-label="Red criminal law book cover"></div>

<div class="abs area-title" style="left:100px;top:1262px">Building &amp; Construction</div>
<div class="abs area-title" style="left:439px;top:1262px">Corporate &amp; Commercial</div>
<div class="abs area-title" style="left:776px;top:1262px">Criminal Law</div>
<p class="abs area-text" style="left:100px;top:1296px">Our team can help draft and advise on building contracts for a home, commercial or industrial buildings, as well as represent on contracts to be negotiated or in the event of a dispute.</p>
<p class="abs area-text" style="left:439px;top:1296px">Our team can help draft and advise on building contracts for a home, commercial or industrial buildings, as well as represent on contracts to be negotiated or in the event of a dispute.</p>
<p class="abs area-text" style="left:776px;top:1296px">Our team can help draft and advise on building contracts for a home, commercial or industrial buildings, as well as represent on contracts to be negotiated or in the event of a dispute.</p>
<div class="abs btn btn-solid" style="left:514px;top:1432px;width:172px">View more areas</div>

<div class="abs about-photo" role="img" aria-label="Lawyer in a gown seated beside a stack of books in a library"></div>
<section class="abs about-band"></section>
<h2 class="abs about-title">About HBM Law</h2>
<p class="abs about-text">HBM Law has been in existence since 1874 originally starting out as the firm Walter Greaves of Ashford Vale. In 1894 Walter Greaves was acquired by Colonel RT Hartley. The firm became known as RT Hartley &amp; Co. until early 1970 when it became Hartley &amp; Co, Hartley Brennan &amp; Co in 1979 and Hartley Brennan &amp; Moss in 1982.</p>
<div class="abs btn btn-line" style="left:950px;top:1836px;width:162px">View more info</div>

<h2 class="abs section-title" style="top:2032px">Case Studies</h2>
<div class="abs title-rule" style="top:2084px"></div>
<p class="abs intro" style="top:2100px">HBM Law has been in existence since 1874 originally starting out as the firm Walter Greaves of Ashford Vale.</p>

<div class="abs case-title" style="left:100px;top:2174px">Lorem ipsum is simply dummy<br>text of the printing</div>
<div class="abs case-title" style="left:457px;top:2174px">Lorem ipsum is simply dummy<br>text of the printing</div>
<div class="abs case-title" style="left:812px;top:2174px">Lorem ipsum is simply dummy<br>text of the printing</div>
<div class="abs case-rule" style="left:100px;top:2236px"></div>
<div class="abs case-rule" style="left:457px;top:2236px"></div>
<div class="abs case-rule" style="left:812px;top:2236px"></div>
<p class="abs area-text" style="left:100px;top:2256px">Lorem Ipsum is simply dummy text of the printing and typesetting industry. Lorem Ipsum has been the industry's standard dummy text ever since the 1500s.</p>
<p class="abs area-text" style="left:457px;top:2256px">Lorem Ipsum is simply dummy text of the printing and typesetting industry. Lorem Ipsum has been the industry's standard dummy text ever since the 1500s.</p>
<p class="abs area-text" style="left:812px;top:2256px">Lorem Ipsum is simply dummy text of the printing and typesetting industry. Lorem Ipsum has been the industry's standard dummy text ever since the 1500s.</p>
<div class="abs btn btn-solid" style="left:508px;top:2395px;width:184px">View more studies</div>

<section class="abs partners" role="img" aria-label="Dimmed photo of colleagues at work in an office"></section>
<h2 class="abs section-title" style="top:2574px;color:#fff">Partners</h2>
<div class="abs title-rule" style="top:2626px;background:#8a8f98"></div>
<p class="abs intro" style="top:2650px;color:#d6d8dc">HBM Law has been in existence since 1874 originally starting out as the firm Walter Greaves of Ashford Vale.</p>
<div class="abs partner" style="left:127px;top:2718px"><div class="ring" role="img" aria-label="Portrait of Peter Brennan"></div><div class="name">Peter Brennan</div></div>
<div class="abs partner" style="left:326px;top:2718px"><div class="ring" role="img" aria-label="Portrait of Mac Moss"></div><div class="name">Mac Moss</div></div>
<div class="abs partner" style="left:520px;top:2718px"><div class="ring" role="img" aria-label="Portrait of Anne Brennan"></div><div class="name">Anne Brennan</div></div>
<div class="abs partner" style="left:714px;top:2718px"><div class="ring" role="img" aria-label="Portrait of Glen Tan Wei"></div><div class="name">Glen Tan Wei</div></div>
<div class="abs partner" style="left:908px;top:2718px"><div class="ring" role="img" aria-label="Portrait of Sara Whitfield"></div><div class="name">Sara Whitfield</div></div>
<div class="abs dots" style="left:580px;top:2920px"><i class="on"></i><i></i><i></i></div>

<section class="abs testimonials"></section>
<h2 class="abs section-title" style="top:3046px">What Our Client's Say</h2>
<div class="abs title-rule" style="top:3098px"></div>
<p class="abs intro" style="top:3118px">HBM Law has been in existence since 1874 originally starting out as the firm Walter Greaves of Ashford Vale.</p>
<div class="abs client-photo" role="img" aria-label="Portrait of client Darren Holloway in a suit"></div>
<div class="abs qmark" style="left:412px;top:3218px">&ldquo;</div>
<p class="abs quote">Lorem ipsum is simply dummy text of the printing and typesetting industry. Lorem Ipsum has been the industry's standard dummy text ever since the 1500s, when an unknown printer took a galley of type and scrambled it to make a type specimen book...</p>
<div class="abs qmark" style="left:1020px;top:3290px">&rdquo;</div>
<div class="abs" style="left:449px;top:3334px;font-size:14px;font-weight:700;color:var(--navy)">Darren Holloway</div>
<div class="abs" style="left:449px;top:3358px;font-size:11.5px;color:#444">Business man</div>
<div class="abs dots" style="left:1008px;top:3358px"><i style="background:#b8bcc3"></i><i style="background:#b8bcc3"></i></div>

<footer class="abs site-footer"></footer>
<div class="abs foot-head" style="left:103px;top:3492px">Who we are?</div>
<p class="abs foot-text" style="left:103px;top:3528px;width:370px">HBM Law has been in existence since 1874 originally starting out as the firm Walter Greaves of Ashford Vale. In 1894 Walter Greaves was acquired by Colonel RT Hartley. The firm became known as RT Hartley &amp; Co...</p>
<div class="abs" style="left:103px;top:3630px;font-size:12px;font-weight:700;color:#fff">Read more info
  <svg width="12" height="12" viewBox="0 0 12 12" style="vertical-align:-2px;margin-left:4px"><circle cx="6" cy="6" r="6" fill="#fff"/><path d="M5 3.5 7.5 6 5 8.5" stroke="#123f7d" stroke-width="1.5" fill="none"/></svg>
</div>
<div class="abs foot-head" style="left:565px;top:3492px">Welcome</div>
<ul class="abs foot-list" style="left:565px;top:3522px"><li>Home</li><li>About Us</li><li>Services</li><li>People</li><li>Community</li><li>Contact Us</li></ul>
<div class="abs foot-head" style="left:761px;top:3492px">Information</div>
<ul class="abs foot-list" style="left:761px;top:3522px"><li>Terms &amp; Conditions</li><li>Privacy policy</li><li>Disclaimer</li><li>Sitemap</li></ul>
<div class="abs foot-brand">HBM</div>

<div class="abs bottom-bar">
  <div class="abs" style="left:103px;top:24px">&copy; 2017, HBM Law. All rights reserved</div>
  <div class="abs" style="left:740px;top:24px">Connect with our social network :</div>
  <div class="abs social" style="left:948px;top:24px"><i></i><i></i><i></i><i></i><i></i></div>
</div>

</body>
</html>
```